Physician focused educational website needed

We are looking to create a fresh, simple website to help Physicians understand the benefits of protecting their largest asset....their income. We are wanting to create a site that can be a resource to help answer the FAQ that physicians ask regarding Disability Insurance. The goal is not to sell DI but rather to education the physician on the importance of the product and to be a resource for them to learn more.

Target Market(s)

Physicians

Industry/Entity Type

Insurance

Coding

Coded - Design and coding required

Number of Pages Required

1 page

Requirements
Must have
• easy to navigate and understand FAQ format

```html
<!DOCTYPE html>
<html lang="en">
<head>
<meta charset="utf-8">
<title>Disability Insurance</title>
<link rel="stylesheet" href="https://fonts.googleapis.com/css2?family=Montserrat:wght@300;400;500;700&display=swap">
<style>
:root{
  --green:#7dc24b;
  --ink:#2b2b2b;
  --text:#555;
  --soft:#f5f5f5;
  --footer:#151515;
  --footer-text:#9a9a9a;
  --white:#fff;
}
*{box-sizing:border-box;margin:0;padding:0}
html,body{width:762px;height:1200px;overflow:hidden}
body{position:relative;font-family:"Montserrat",sans-serif;color:var(--ink);background:var(--white)}
.abs{position:absolute}

/* header */
.site-header{position:absolute;top:0;left:0;width:762px;height:39px;background:var(--white);z-index:2}
.brand{left:51px;top:14px;font-size:8.5px;font-weight:700;letter-spacing:.6px;color:#333}
.main-nav{left:364px;top:14px;display:flex;gap:17px;font-size:8px;color:#444}
.main-nav a{color:inherit;text-decoration:none}
.share{left:622px;top:14px}
.blog-link{left:660px;top:14px;font-size:8px;color:#444}
.menu{left:740px;top:14px}

/* hero */
.hero{top:39px;left:0;width:762px;height:336px;
  background:linear-gradient(100deg,#3b4149 0%,#52585e 30%,#3f4347 55%,#2c2f34 80%,#3a3f45 100%)}
.hero-shade{top:39px;left:0;width:762px;height:336px;background:rgba(0,0,0,.25)}
.hero-title{top:174px;left:0;width:762px;text-align:center;color:var(--white);font-size:17px;font-weight:400;letter-spacing:.6px}
.hero-sub{top:210px;left:0;width:762px;text-align:center;color:#e8e8e8;font-size:8.5px;font-weight:300}
.hero-btn{top:245px;left:314px;width:134px;height:37px;background:var(--green);color:var(--white);font-size:8.5px;display:flex;align-items:center;justify-content:center}

/* features */
.feature{top:445px;width:200px;text-align:center}
.feature-icon{display:block;margin:0 auto;width:42px;height:42px}
.feature-title{margin-top:15px;font-size:11.5px;font-weight:400;color:#333;letter-spacing:.2px}
.feature-text{margin-top:6px;font-size:8.5px;line-height:17px;color:var(--text);font-weight:400}
.continue{display:inline-block;margin-top:15px;border:1px solid #333;font-size:6px;padding:5px 6px;color:#333;letter-spacing:.2px}

/* faq */
.faq{top:661px;left:0;width:762px;height:297px;background:var(--soft)}
.faq-title{top:730px;left:0;width:762px;text-align:center;font-size:13.5px;font-weight:400;letter-spacing:.6px;color:#333}
.faq-item{display:flex;gap:9px;font-size:11px;line-height:17px;color:#444;font-weight:400}
.faq-item svg{flex:none;margin-top:2px}

/* footer */
.site-footer{top:958px;left:0;width:762px;height:242px;background:var(--footer)}
.foot-head{top:1002px;font-size:8.5px;color:var(--white);font-weight:500}
.foot-list{top:1024px;list-style:none;font-size:7.5px;color:var(--footer-text)}
.foot-list li{height:20px;display:flex;align-items:center;gap:7px}
.tweets{top:1024px;left:390px;font-size:7.5px;line-height:17px;color:var(--footer-text)}
.address{top:1024px;left:554px;font-size:7.5px;line-height:17px;color:var(--footer-text)}
.email-head{top:1090px;left:554px;font-size:8.5px;color:var(--white)}
.email{top:1107px;left:554px;font-size:7.5px;color:var(--footer-text)}
.social{top:1150px;left:318px;display:flex;gap:9px}
.social span{width:9px;height:9px;border-radius:50%;background:#a5a5a5}
.copyright{top:1175px;left:0;width:762px;text-align:center;font-size:6px;color:var(--footer-text)}
</style>
</head>
<body>

<header class="site-header">
  <div class="abs brand">DISABILITY INSURANCE</div>
  <nav class="abs main-nav">
    <a href="#">Disability Insurance</a><a href="#">Guidelines</a><a href="#">Faq</a><a href="#">Contact Us</a>
  </nav>
  <svg class="abs share" width="9" height="9" viewBox="0 0 9 9" aria-label="Share"><circle cx="7" cy="1.6" r="1.4" fill="#444"/><circle cx="2" cy="4.5" r="1.4" fill="#444"/><circle cx="7" cy="7.4" r="1.4" fill="#444"/><path d="M7 1.6 2 4.5 7 7.4" stroke="#444" fill="none" stroke-width=".9"/></svg>
  <div class="abs blog-link">Blog</div>
  <svg class="abs menu" width="13" height="11" viewBox="0 0 13 11" aria-label="Menu"><rect y="0" width="13" height="2" fill="#222"/><rect y="4.5" width="13" height="2" fill="#222"/><rect y="9" width="13" height="2" fill="#222"/></svg>
</header>

<section>
  <div class="abs hero" role="img" aria-label="Photo of a physician helping a colleague in a wheelchair at an office desk"></div>
  <div class="abs hero-shade"></div>
  <h1 class="abs hero-title">Disability Insurance</h1>
  <p class="abs hero-sub">Protect your income with our affordable disability plans</p>
  <div class="abs hero-btn">Request Information</div>
</section>

<section>
  <div class="abs feature" style="left:61px">
    <svg class="feature-icon" viewBox="0 0 42 42"><circle cx="21" cy="21" r="21" fill="var(--green)"/><path d="M15 11h8l5 5v15H15z" fill="#fff"/><path d="M23 11v5h5" fill="#cfe8bb"/><path d="M18 20h7M18 23h7M18 26h7" stroke="var(--green)" stroke-width="1.3"/></svg>
    <h2 class="feature-title">DI Guide</h2>
    <p class="feature-text">Claritas est etiam processus dynamicus, qui sequitur mutationem consuetudium</p>
    <span class="continue">CONTINUE</span>
  </div>
  <div class="abs feature" style="left:281px">
    <svg class="feature-icon" viewBox="0 0 42 42"><circle cx="21" cy="21" r="21" fill="var(--green)"/><text x="21" y="29" text-anchor="middle" font-family="Montserrat,sans-serif" font-weight="700" font-size="22" fill="#fff">$</text></svg>
    <h2 class="feature-title">Protect Your Income</h2>
    <p class="feature-text">Claritas est etiam processus dynamicus, qui sequitur mutationem consuetudium</p>
    <span class="continue">CONTINUE</span>
  </div>
  <div class="abs feature" style="left:501px">
    <svg class="feature-icon" viewBox="0 0 42 42"><circle cx="21" cy="21" r="21" fill="var(--green)"/><circle cx="21" cy="21" r="10" fill="#fff"/><text x="21" y="25.5" text-anchor="middle" font-family="Montserrat,sans-serif" font-weight="700" font-size="13" fill="var(--green)">?</text></svg>
    <h2 class="feature-title">Features</h2>
    <p class="feature-text">Claritas est etiam processus dynamicus, qui sequitur mutationem consuetudium</p>
    <span class="continue">CONTINUE</span>
  </div>
</section>

<section>
  <div class="abs faq"></div>
  <h2 class="abs faq-title">FREQUENTLY ASKED QUESTIONS</h2>
  <div class="abs faq-item" style="left:59px;top:794px"><svg width="15" height="15" viewBox="0 0 15 15"><rect x=".6" y=".6" width="13.8" height="13.8" fill="none" stroke="#333" stroke-width="1.2"/><path d="M7.5 3.5v8M3.5 7.5h8" stroke="#333" stroke-width="1.2"/></svg>What if my health changes after I buy coverage?</div>
  <div class="abs faq-item" style="left:59px;top:823px"><svg width="15" height="15" viewBox="0 0 15 15"><rect x=".6" y=".6" width="13.8" height="13.8" fill="none" stroke="#333" stroke-width="1.2"/><path d="M7.5 3.5v8M3.5 7.5h8" stroke="#333" stroke-width="1.2"/></svg>What features should I look for?</div>
  <div class="abs faq-item" style="left:59px;top:852px"><svg width="15" height="15" viewBox="0 0 15 15"><rect x=".6" y=".6" width="13.8" height="13.8" fill="none" stroke="#333" stroke-width="1.2"/><path d="M7.5 3.5v8M3.5 7.5h8" stroke="#333" stroke-width="1.2"/></svg>What is Catestrophic Benefit?</div>
  <div class="abs faq-item" style="left:389px;top:794px"><svg width="15" height="15" viewBox="0 0 15 15"><rect x=".6" y=".6" width="13.8" height="13.8" fill="none" stroke="#333" stroke-width="1.2"/><path d="M7.5 3.5v8M3.5 7.5h8" stroke="#333" stroke-width="1.2"/></svg>Can I raise my coverage after I enter practice?</div>
  <div class="abs faq-item" style="left:389px;top:823px"><svg width="15" height="15" viewBox="0 0 15 15"><rect x=".6" y=".6" width="13.8" height="13.8" fill="none" stroke="#333" stroke-width="1.2"/><path d="M7.5 3.5v8M3.5 7.5h8" stroke="#333" stroke-width="1.2"/></svg>What is true own occupation/specialty specific mean?</div>
  <div class="abs faq-item" style="left:389px;top:852px;width:330px"><svg width="15" height="15" viewBox="0 0 15 15"><rect x=".6" y=".6" width="13.8" height="13.8" fill="none" stroke="#333" stroke-width="1.2"/><path d="M7.5 3.5v8M3.5 7.5h8" stroke="#333" stroke-width="1.2"/></svg>What is DIRS? (disability income retirement supplement)</div>
</section>

<footer>
  <div class="abs site-footer"></div>
  <h3 class="abs foot-head" style="left:59px">Popular Articles</h3>
  <ul class="abs foot-list" style="left:59px">
    <li><svg width="7" height="8" viewBox="0 0 7 8"><path d="M.5.5h4l2 2v5H.5z" fill="none" stroke="#888" stroke-width=".8"/></svg>Lorem ipsum dolor sit amet</li>
    <li><svg width="7" height="8" viewBox="0 0 7 8"><path d="M.5.5h4l2 2v5H.5z" fill="none" stroke="#888" stroke-width=".8"/></svg>Lorem ipsum dolor</li>
    <li><svg width="7" height="8" viewBox="0 0 7 8"><path d="M.5.5h4l2 2v5H.5z" fill="none" stroke="#888" stroke-width=".8"/></svg>Lorem ipsum dolor sit amet</li>
    <li><svg width="7" height="8" viewBox="0 0 7 8"><path d="M.5.5h4l2 2v5H.5z" fill="none" stroke="#888" stroke-width=".8"/></svg>Lorem ipsum dolor</li>
  </ul>
  <h3 class="abs foot-head" style="left:224px">Recent Blogs</h3>
  <ul class="abs foot-list" style="left:224px">
    <li><svg width="7" height="8" viewBox="0 0 7 8"><path d="M.5.5h4l2 2v5H.5z" fill="none" stroke="#888" stroke-width=".8"/></svg>Lorem ipsum dolor</li>
    <li><svg width="7" height="8" viewBox="0 0 7 8"><path d="M.5.5h4l2 2v5H.5z" fill="none" stroke="#888" stroke-width=".8"/></svg>Lorem ipsum dolor sit amet</li>
    <li><svg width="7" height="8" viewBox="0 0 7 8"><path d="M.5.5h4l2 2v5H.5z" fill="none" stroke="#888" stroke-width=".8"/></svg>Lorem ipsum dolor</li>
    <li><svg width="7" height="8" viewBox="0 0 7 8"><path d="M.5.5h4l2 2v5H.5z" fill="none" stroke="#888" stroke-width=".8"/></svg>Lorem ipsum dolor sit amet</li>
  </ul>
  <h3 class="abs foot-head" style="left:390px">Latest Tweets</h3>
  <div class="abs tweets">
    Lorem ipsum dolor sit amet,<br>consectetur adipiscing elit, sed do...<br>@brightwell http://brightwellstudio.net<br>
    Lorem ipsum dolor sit amet,<br>consectetur adipiscing elit, sed do...<br>@brightwell http://brightwellstudio.net
  </div>
  <h3 class="abs foot-head" style="left:554px">Address</h3>
  <div class="abs address">27 Maple Court, Beside Harbor<br>Plaza, Riverton, USA<br>40512</div>
  <h3 class="abs email-head">Email ID</h3>
  <div class="abs email">hello@brightwellstudio.net</div>
  <div class="abs social" aria-label="Social links"><span></span><span></span><span></span><span></span><span></span><span></span><span></span><span></span></div>
  <div class="abs copyright">© 2016 Build By Brightwell Studio</div>
</footer>

</body>
</html>
```